Flyer for language school

Hi,
We are language school, we offre german courses.
We will provide our students with a notepad during registration in a german course.
For that, we need the front page ofthe notepad to be pretty, simple and remarkable.
U can find our colors in the logo in the attachement.
for the contact information, we need those three adresses
Tunis - Imm Les Cyprès, 3ème étage 47 Rue des Palmiers Bleus, 1053 Les Berges du Lac 1
Tél : 71 482 613
Email : tunis@vorlinda.org
Sfax - Imm Zahrat, 5ème étage Rue Slim Bouraoui (en face de la crvp), 3027 Sfax
Tél : 74 613 952
Email : sfax@vorlinda.org
Sousse - 54 Ave Tahar Kelibi (prés du rond point Belvista au dessus du café Myrtille).
Tél : 73 590 126
Email : sousse@vorlinda.org
The website needs to be cited also :
www.vorlinda.org
School

```html
<!DOCTYPE html>
<html lang="fr">
<head>
<meta charset="utf-8">
<title>Vorlinda – Bloc-notes</title>
<link rel="stylesheet" href="https://fonts.googleapis.com/css2?family=Libre+Franklin:wght@600;700&display=swap">
<style>
  :root {
    --ink: #000000;
    --paper: #ffffff;
    --name-ink: #231f20;
    --tone-deep: #d8cf10;
    --tone-bright: #f9e81e;
    --tone-pale: #fffbd2;
    --brand-dot: #dcd61c;
    --contact-ink: #ffffff;
  }
  html, body {
    margin: 0;
    padding: 0;
    overflow: hidden;
    background: var(--paper);
  }
  .notepad-cover {
    position: relative;
    width: 927px;
    height: 1200px;
    overflow: hidden;
    background: var(--paper);
    font-family: "Libre Franklin", Arial, sans-serif;
  }
  .cover-backdrop {
    position: absolute;
    inset: 0;
    width: 927px;
    height: 1200px;
  }
  .brand {
    position: absolute;
    top: 150px;
    left: 640px;
    display: flex;
    align-items: center;
    gap: 12px;
  }
  .brand-dot {
    width: 22px;
    height: 22px;
    border-radius: 50%;
    background: var(--brand-dot);
  }
  .brand-name {
    font-size: 54px;
    font-weight: 700;
    letter-spacing: -1px;
    color: var(--name-ink);
    line-height: 1;
  }
  .contacts {
    position: absolute;
    left: 46px;
    top: 764px;
    width: 260px;
    color: var(--contact-ink);
    font-size: 14px;
    font-weight: 600;
    line-height: 19px;
  }
  .office {
    margin: 0 0 19px;
  }
  .website {
    margin: 0;
    font-weight: 700;
  }
</style>
</head>
<body>
<main class="notepad-cover">
  <svg class="cover-backdrop" viewBox="0 0 927 1200" role="img" aria-label="Decorative sweep of layered yellow curved bands rising from a black corner">
    <defs>
      <linearGradient id="sweepTone" gradientUnits="userSpaceOnUse" x1="0" y1="1100" x2="700" y2="200">
        <stop offset="0" stop-color="var(--ink)"/>
        <stop offset="0.44" stop-color="var(--ink)"/>
        <stop offset="0.56" stop-color="var(--tone-deep)"/>
        <stop offset="0.75" stop-color="var(--tone-bright)"/>
        <stop offset="1" stop-color="var(--tone-pale)"/>
      </linearGradient>
    </defs>
    <path class="sweep-area" d="M0,0 C520,60 815,520 825,1200 L0,1200 Z" fill="url(#sweepTone)"/>
  </svg>

  <div class="brand">
    <span class="brand-dot"></span>
    <span class="brand-name">vorlinda</span>
  </div>

  <section class="contacts">
    <p class="office">Tunis - Imm Les Cyprès, 3ème<br>étage 47 Rue des Palmiers Bleus,<br>1053 Les Berges du Lac 1<br>Tél : 71 482 613<br>Email : tunis@vorlinda.org</p>
    <p class="office">Sfax - Imm Zahrat, 5ème étage<br>Rue Slim Bouraoui (en face de la<br>crvp), 3027 Sfax<br>Tél : 74 613 952<br>Email : sfax@vorlinda.org</p>
    <p class="office">Sousse - 54 Ave Tahar Kelibi<br>(prés du rond point<br>Belvista au dessus du café<br>Myrtille).<br>Tél : 73 590 126<br>Email : sousse@vorlinda.org</p>
    <p class="website">www.vorlinda.org</p>
  </section>
</main>
</body>
</html>
```